Small B&W Ear Panel Spa Newspaper Ad

We need a redesign for our Daily Ear Panel Newspaper Advertisement which appears in Harbor Ledger daily newspaper in Dubai.
The advert is small, size 40mm x 25mm, and it is in B&W, or black, grey and white.
The advert is for Willowstone Spa and Massage Centres.
We attach the current pdf file which we use - the information included in the current ad is :
willowstone
Balinese Massage Centres
Spa
800 KNEADER
British Owned & Managed
www.willowstone-example.ae
The advert is very small, and the MINIMUM information we would like to include is :
willowstone
Spa
800 KNEADER
ww.willowstone-example.ae
It is optional to include the extra information :
Balinese Massage Centres
British Owned & Managed
The main brief is that the Advert must be BOLD & EYE-CATCHING.
iT MAY BE BEST TO KEEP THE ADVERT SIMPLE IN ORDER TO ACHIEVE THIS.
We like the current "rounded" edges to the box.
It may be best to use shades of black, grey and white.
We attach also 2 pictures of the front page of the Newspaper so that you can see how the Ad sits on the page, and how small it is.
The advert appears every day, so it must also be memorable, so that readers become used to it, whilst it still attracts their attention.
ONE POSSIBLE IDEA - PERHAPS THE ADVERT CAN BE A CIRCULAR, ROUND OR OVAL DESIGN, WHICH WOULD GIVE MORE BLANK WHITE SPACE AROUND IT, SO THAT IT WOULD STAND OUT MORE.

```html
<!DOCTYPE html>
<html lang="en">
<head>
<meta charset="utf-8">
<title>Willowstone Spa – Ear Panel Ad</title>
<link rel="stylesheet" href="https://fonts.googleapis.com/css2?family=Arimo:ital,wght@0,700;1,400&family=Anton&display=swap">
<style>
  :root {
    --page: #ffffff;
    --panel: #3b3b3b;
    --ink: #ffffff;
    --outline: #111111;
    --mark-grey: #9a9a9a;
  }
  html, body {
    margin: 0;
    padding: 0;
    width: 1200px;
    height: 749px;
    overflow: hidden;
    background: var(--page);
  }
  .ad {
    position: relative;
    width: 1200px;
    height: 749px;
  }
  .ad-panel {
    position: absolute;
    left: 5px;
    top: 5px;
    width: 1190px;
    height: 739px;
    border-radius: 56px;
    background: var(--panel);
  }
  .brand-row {
    position: absolute;
    left: 0;
    top: 12px;
    width: 1200px;
    display: flex;
    justify-content: center;
    align-items: center;
    gap: 22px;
  }
  .brand-name {
    font-family: "Arimo", Arial, sans-serif;
    font-weight: 700;
    font-size: 122px;
    line-height: 1;
    color: var(--ink);
    letter-spacing: -1px;
  }
  .brand-mark {
    width: 104px;
    height: 104px;
    background: var(--mark-grey);
    margin-top: 10px;
  }
  .service {
    position: absolute;
    left: 0;
    top: 178px;
    width: 1200px;
    text-align: center;
    font-family: "Arimo", Arial, sans-serif;
    font-style: italic;
    font-weight: 400;
    font-size: 172px;
    line-height: 1;
    color: var(--ink);
  }
  .phone-line {
    position: absolute;
    left: 0;
    top: 360px;
    width: 1200px;
    height: 190px;
  }
  .website {
    position: absolute;
    left: 0;
    top: 612px;
    width: 1200px;
    text-align: center;
    font-family: "Arimo", Arial, sans-serif;
    font-weight: 700;
    font-size: 78px;
    line-height: 1;
    color: var(--ink);
  }
</style>
</head>
<body>
  <main class="ad">
    <div class="ad-panel"></div>

    <div class="brand-row">
      <span class="brand-name">willowstone</span>
      <span class="brand-mark" role="img" aria-label="Willowstone brand mark"></span>
    </div>

    <div class="service">Spa</div>

    <svg class="phone-line" viewBox="0 0 1200 190" aria-label="Call 800 KNEADER">
      <g class="phone-icon" fill="var(--ink)" stroke="var(--outline)" stroke-width="5" stroke-linejoin="round">
        <path d="M142 62 C150 22 262 22 272 62 L272 80 L236 80 L232 66 L182 66 L178 80 L142 80 Z"/>
        <path d="M182 74 L232 74 L268 150 L146 150 Z"/>
        <g fill="var(--outline)" stroke="none">
          <rect x="184" y="94" width="12" height="9"/>
          <rect x="201" y="94" width="12" height="9"/>
          <rect x="218" y="94" width="12" height="9"/>
          <rect x="180" y="110" width="13" height="9"/>
          <rect x="201" y="110" width="12" height="9"/>
          <rect x="221" y="110" width="13" height="9"/>
          <rect x="176" y="126" width="14" height="9"/>
          <rect x="200" y="126" width="14" height="9"/>
          <rect x="224" y="126" width="14" height="9"/>
        </g>
      </g>
      <g class="phone-number" font-family="Anton, Impact, sans-serif" font-size="158" text-anchor="start">
        <text x="290" y="160" fill="var(--ink)" stroke="var(--ink)" stroke-width="22" stroke-linejoin="round" textLength="840" lengthAdjust="spacingAndGlyphs">800 KNEADER</text>
        <text x="290" y="160" fill="var(--ink)" stroke="var(--outline)" stroke-width="12" stroke-linejoin="round" textLength="840" lengthAdjust="spacingAndGlyphs">800 KNEADER</text>
        <text x="290" y="160" fill="var(--ink)" textLength="840" lengthAdjust="spacingAndGlyphs">800 KNEADER</text>
      </g>
    </svg>

    <div class="website">www.willowstone-example.ae</div>
  </main>
</body>
</html>
```